Business card design needed

We require a business card and logo design for our tipper truck business which services the building and agricultural industries, based in Albury-Wodonga, Australia. The business name is 'Falcon Haulage' and our business moto is 'if it's tippable, it's doable'.
If a tipper truck is to be included in the logo, the truck must not have a nose ie. the truck must have a flat front.
The moto for the Albury-Wodonga region is 'where the mountains meet the murray' (snowy mountains meet murray river-this may or may not be included in the image design)

Industry/Entity Type

Building

Contact Information for Business Card

FALCON HAULAGE PTY LTD
Complete Dumping Solutions
If it's tippable, it's doable!
Col Brimble
0483 906 217
falconhaulage@quillmail.com.au
PO Box 829
Fernvale NSW 2739
ABN: 57 309 842 615

```html
<!DOCTYPE html>
<html lang="en">
<head>
<meta charset="utf-8">
<title>Falcon Haulage – Business Cards</title>
<link rel="stylesheet" href="https://fonts.googleapis.com/css2?family=Open+Sans:wght@400;600;800&family=Cormorant+Garamond:wght@500&display=swap">
<style>
  :root {
    --page-bg: #e4e4e2;
    --night-teal: #1f5566;
    --night-deep: #0d2630;
    --night-black: #050708;
    --sky-top: #8fb0c4;
    --sky-low: #c9dce6;
    --snow: #e8eef1;
    --brand-blue: #1f6fb5;
    --band-orange: #ea6a1f;
    --ink: #1d1d1d;
    --white: #ffffff;
    --panel-light: #f6f6f6;
    --panel-grey: #dcdcdc;
  }
  * { box-sizing: border-box; margin: 0; padding: 0; }
  html, body { width: 900px; height: 1200px; overflow: hidden; }
  body { background: var(--page-bg); position: relative; font-family: "Open Sans", sans-serif; }

  .card { position: absolute; width: 738px; height: 442px; overflow: hidden; box-shadow: 0 6px 18px rgba(0,0,0,.25); }

  /* Front card */
  .card--front { left: 35px; top: 133px; }
  .front-scene {
    position: absolute; inset: 0;
    background:
      linear-gradient(180deg, rgba(0,0,0,0) 55%, var(--night-black) 78%),
      radial-gradient(ellipse at 80% 70%, #4d8fa0 0%, var(--night-teal) 35%, var(--night-deep) 75%);
  }
  .front-brand {
    position: absolute; left: 0; right: 0; top: 118px;
    text-align: center; color: var(--white);
    font-weight: 800; font-size: 76px; letter-spacing: 1px;
  }
  .front-motto {
    position: absolute; left: 72px; bottom: 22px;
    color: var(--white); font-family: "Cormorant Garamond", serif;
    font-weight: 500; font-size: 40px; transform: scaleX(.88); transform-origin: left;
    white-space: nowrap;
  }

  /* Back card */
  .card--back { left: 132px; top: 621px; height: 441px; }
  .back-scene {
    position: absolute; left: 0; top: 0; width: 738px; height: 287px;
    background: linear-gradient(180deg, var(--sky-top) 0%, var(--sky-low) 70%, var(--snow) 100%);
  }
  .back-brand {
    position: absolute; left: 14px; top: 34px;
    color: var(--brand-blue); font-weight: 800; font-size: 40px;
  }
  .truck-art {
    position: absolute; left: 378px; top: 124px; width: 345px; height: 162px;
    background: linear-gradient(180deg, #fafafa 0%, #e3e6e8 75%, #6b6f72 100%);
    border-radius: 4px;
  }
  .name-band {
    position: absolute; left: 0; top: 287px; width: 738px; height: 60px;
    background: var(--band-orange); border-top: 2px solid #c85515;
    color: var(--white); font-size: 37px; font-weight: 400; letter-spacing: 3.5px;
    line-height: 58px; padding-left: 14px; white-space: nowrap;
  }
  .contact-panel {
    position: absolute; left: 0; top: 347px; width: 738px; height: 94px;
    background: linear-gradient(180deg, var(--panel-light), var(--panel-grey));
    display: grid; grid-template-columns: 386px 1fr; row-gap: 16px;
    padding: 18px 0 0 14px;
  }
  .contact-item { display: flex; align-items: center; gap: 8px; color: var(--ink); font-size: 16px; letter-spacing: .4px; white-space: nowrap; }
  .contact-item--wide { font-size: 17px; }
  .contact-item svg { flex: none; }
</style>
</head>
<body>

<section class="card card--front">
  <div class="front-scene" role="img" aria-label="Dusk sky over a dark silhouetted mountain range"></div>
  <div class="front-brand">Falcon Haulage</div>
  <p class="front-motto">If it’s tippable, it’s doable! Col Brimble</p>
</section>

<section class="card card--back">
  <div class="back-scene" role="img" aria-label="Pale sky above snowy mountain peaks"></div>
  <div class="back-brand">Falcon Haulage</div>
  <div class="truck-art" role="img" aria-label="Flat-fronted white box truck carrying the company name and motto"></div>
  <div class="name-band">FALCON HAULAGE LTD</div>

  <div class="contact-panel">
    <div class="contact-item">
      <svg width="18" height="24" viewBox="0 0 18 24" aria-hidden="true"><rect x="2" y="1" width="14" height="22" rx="3" fill="#1d1d1d"/><rect x="4.5" y="4" width="9" height="12" fill="#dcdcdc"/></svg>
      <span>0483906217</span>
    </div>
    <div class="contact-item contact-item--wide">
      <svg width="26" height="18" viewBox="0 0 26 18" aria-hidden="true"><rect x="1" y="1" width="24" height="16" fill="#1d1d1d"/><path d="M1 1 L13 10 L25 1" fill="none" stroke="#f2f2f2" stroke-width="1.6"/></svg>
      <span>falconhaulage@quillmail.com.au</span>
    </div>
    <div class="contact-item">
      <svg width="18" height="18" viewBox="0 0 18 18" aria-hidden="true"><circle cx="9" cy="9" r="8" fill="#1d1d1d"/><path d="M9 4 a3 3 0 0 1 3 3 c0 2.4-3 6-3 6 s-3-3.6-3-6 a3 3 0 0 1 3-3z" fill="#f2f2f2"/></svg>
      <span>PO Box 829 Fernvale NSW 2739</span>
    </div>
    <div class="contact-item contact-item--wide">
      <svg width="26" height="22" viewBox="0 0 26 22" aria-hidden="true"><circle cx="13" cy="6" r="5.5" fill="#1d1d1d"/><path d="M3 22 c0-7 4-9.5 10-9.5 s10 2.5 10 9.5z" fill="#1d1d1d"/></svg>
      <span>ABN:57 309 842 615</span>
    </div>
  </div>
</section>

</body>
</html>
```